VALMIKE GROUP

This is a company that provides executive protection. Our motto is "New Era in Protection"... I don't want this to look like other security websites. I want it to be clean and sharp and represent a new era. We are based in the bay area so maybe a picture of San Francisco in the background?
I want it to be able to funnel down a couple different categories.
1. About Us
2. Services (Executive Protection, Covert Protection, Residential Protection & Intelligence)
3. Iron Finch (Training & Consulting)
4. Contact Us
I want it to be very clean and modern. I don't want there to be any pictures of bodyguards with ear pieces like every other website.
Target Market(s)
Ultra High Net Worth Individuals
Coding
Coded - Design and coding required
Number of Pages Required
1 page
Requirements
Must have
- Colors of my Symbol
Nice to have
- City in the background, San Francisco, New York or the Pinehallow Club in Montana.
Should not have
- Should not look like an KVM website or have photos of bodyguards. I want this to be a clean and simple website with my logo

```html
<!DOCTYPE html>
<html lang="en">
<head>
<meta charset="utf-8">
<title>VALMIKE GROUP — New Era in Protection</title>
<link rel="stylesheet" href="https://fonts.googleapis.com/css2?family=Orbitron:wght@700;900&family=Poppins:wght@400;500;600;700&display=swap">
<style>
:root{
  --red:#8e1316;
  --red-deep:#7a0f12;
  --ink:#111111;
  --text:#555555;
  --muted:#8a8a8a;
  --field:#ececec;
  --white:#ffffff;
  --footer:#050505;
  --display:'Orbitron',sans-serif;
  --body:'Poppins',sans-serif;
}
*{margin:0;padding:0;box-sizing:border-box}
html,body{width:1200px;height:4291px;overflow:hidden;background:var(--white)}
body{font-family:var(--body);color:var(--text)}
.page{position:relative;width:1200px;height:4291px;overflow:hidden}
.abs{position:absolute}

/* header & hero */
.hero-bg{left:0;top:0;width:1200px;height:842px;
  background:linear-gradient(180deg,#1f3c4a 0%,#3a5560 25%,#5a5a4c 45%,#3e4a4c 65%,#1e2d36 100%)}
.hero-cut{left:0;top:0}
.brand{display:flex;align-items:center;gap:14px;font-family:var(--body);font-weight:600;color:var(--white);font-size:22px;letter-spacing:2px}
.brand-mark{width:40px;height:40px;background:var(--red)}
.nav{top:44px;left:499px;display:flex;gap:0;align-items:center}
.nav a{font-family:var(--body);font-weight:700;font-size:14px;color:var(--white);text-decoration:none;text-transform:uppercase}
.nav-cta{left:972px;top:34px;width:135px;height:41px;background:var(--red);display:flex;align-items:center;justify-content:center;font-weight:700;font-size:14px;color:var(--white)}
.hero-title{left:92px;top:360px;font-family:var(--display);font-weight:900;color:var(--white);text-transform:uppercase;letter-spacing:2px}
.hero-title .l1{display:block;font-size:56px;line-height:66px}
.hero-title .l2{display:block;font-size:80px;line-height:86px}
.scroll-cue{left:582px;top:720px}

/* headings */
.eyebrow{font-family:var(--display);font-weight:700;font-size:24px;color:var(--red);text-transform:uppercase;letter-spacing:1px;line-height:28px}
.heading{font-family:var(--display);font-weight:900;font-size:38px;color:var(--ink);text-transform:uppercase;letter-spacing:2px;line-height:44px}
.center{text-align:center;left:0;width:1200px}
.copy{font-size:16px;line-height:24px;color:var(--text)}
.btn{display:flex;align-items:center;justify-content:center;font-weight:700;font-size:14px;text-transform:uppercase}
.btn-red{background:var(--red);color:var(--white)}

/* about */
.photo{box-shadow:0 20px 40px rgba(0,0,0,.25)}
.photo-exec{left:138px;top:870px;width:227px;height:423px;background:linear-gradient(160deg,#5d6872,#2e3338 60%,#474240)}
.photo-bridge{left:373px;top:978px;width:175px;height:362px;background:linear-gradient(180deg,#2a2220,#8a6a4a 45%,#c7884e 55%,#3a3230)}
.about-text{left:618px;top:1015px;width:500px}
.about-text .copy{margin-top:14px}
.about-btn{margin-top:24px;width:135px;height:38px}

/* services */
.card{top:1555px;width:330px;height:460px;background:var(--white);box-shadow:0 6px 26px rgba(0,0,0,.10)}
.card-img{height:278px}
.card-body{padding:22px 34px}
.card-title{font-weight:700;font-size:20px;line-height:22px;color:var(--ink);text-transform:uppercase}
.card-body .copy{margin-top:14px}

/* iron finch band */
.band{left:0;top:2100px}
.band-art{left:650px;top:2200px;width:550px;height:470px}
.band-text{left:88px;top:2298px;width:600px;color:var(--white)}
.band-eyebrow{font-family:var(--display);font-weight:700;font-size:22px;letter-spacing:1px;text-transform:uppercase}
.band-title{margin-top:12px;font-family:var(--display);font-weight:900;font-size:35px;line-height:36px;letter-spacing:2px;text-transform:uppercase}
.band-text .copy{margin-top:18px;color:#f1dede;width:585px}
.band-btn{margin-top:36px;width:137px;height:40px;background:var(--white);color:var(--red)}

/* testimonials */
.avatar{left:547px;top:2855px;width:106px;height:106px;border-radius:50%;background:linear-gradient(160deg,#d5dde2,#8b99a2)}
.quote{left:252px;top:2900px;font-family:Georgia,serif;font-size:240px;line-height:240px;color:#e0e0e0}
.reviewer{top:2975px;font-weight:600;font-size:20px;color:var(--ink)}
.role{top:3004px;font-weight:600;font-size:11px;color:var(--red);letter-spacing:1px}
.review{left:270px;top:3036px;width:660px;text-align:center;font-size:16px;line-height:23px;color:var(--text)}
.dots{left:576px;top:3120px;display:flex;gap:8px}
.dots span{width:10px;height:10px;border-radius:50%;background:#d0d0d0}
.dots span.on{background:var(--red)}
.rule{left:87px;top:3210px;width:1020px;height:1px;background:#e4e4e4}

/* contact */
.contact-photo{left:0;top:3233px;width:620px;height:600px;background:linear-gradient(90deg,#b6c0c6 0%,#a63a30 30%,#c8d0d4 70%,rgba(255,255,255,0) 100%)}
.contact-head{left:575px;top:3290px}
.contact-intro{left:575px;top:3362px;font-size:14px;color:#333}
.field{background:var(--field);font-weight:600;font-size:14px;color:#666;padding:10px 20px}
.submit{left:773px;top:3662px;width:139px;height:41px}

/* footer */
.footer{left:0;top:3800px}
.footer-brand{left:133px;top:4022px}
.socials{left:208px;top:4093px;display:flex;gap:8px}
.socials span{width:24px;height:24px;border-radius:50%}
.col{top:3952px}
.col-title{font-weight:600;font-size:17px;color:#6e6e6e;text-transform:uppercase}
.col ul{list-style:none;margin-top:22px}
.col li{font-size:13px;line-height:27px;color:#d8d8d8}
.contact-item{position:relative;padding-left:22px;margin-bottom:20px}
.contact-item b{display:block;font-weight:500;font-size:12px;color:var(--white)}
.contact-item span{display:block;font-size:14px;line-height:17px;color:#d8d8d8}
.contact-item svg{position:absolute;left:0;top:2px}
.footer-rule{left:87px;top:4230px;width:1020px;height:1px;background:#2a2a2a}
.copyright{top:4252px;font-size:13px;color:#d8d8d8}
.to-top{left:1130px;top:4207px}
</style>
</head>
<body>
<div class="page">

  <!-- hero -->
  <div class="abs hero-bg" role="img" aria-label="Golden Gate Bridge at dusk over misty water with rocky shore"></div>
  <svg class="abs hero-cut" width="1200" height="842" viewBox="0 0 1200 842" aria-hidden="true">
    <polygon points="0,842 600,768 1200,842" fill="#ffffff"/>
  </svg>
  <div class="abs brand" style="left:95px;top:22px"><span class="brand-mark"></span>VALMIKE GROUP</div>
  <nav class="abs nav">
    <a href="#" style="margin-right:48px">Home</a>
    <a href="#" style="margin-right:48px">About Us</a>
    <a href="#" style="margin-right:48px">Our Services</a>
    <a href="#">Iron Finch</a>
  </nav>
  <a class="abs nav-cta" href="#">CONTACT US</a>
  <h1 class="abs hero-title"><span class="l1">New Era In</span><span class="l2">Protection</span></h1>
  <svg class="abs scroll-cue" width="50" height="50" viewBox="0 0 50 50" aria-hidden="true">
    <rect x="10" y="10" width="30" height="30" transform="rotate(45 25 25)" fill="none" stroke="#fff" stroke-width="1.6"/>
    <polyline points="22,18 29,25 22,32" fill="none" stroke="#fff" stroke-width="1.6"/>
  </svg>

  <!-- about -->
  <div class="abs photo photo-exec" role="img" aria-label="Executive in a suit raising a hand"></div>
  <div class="abs photo photo-bridge" role="img" aria-label="Bridge deck seen through a framed opening at sunset"></div>
  <div class="abs about-text">
    <div class="eyebrow">About</div>
    <div class="heading">Valmike Group</div>
    <p class="copy">Sed do eiusmod tempor incididunt ut labore et dolore magna aliqua. Ut enim ad minim veniam, quis derit in voluptate velit esse cillum dolore eu fugiat nullautur. Excepteur sint occaecat non proident, sunt in culpa qui officia deserunt Mollit anim id est laborum. Sed ut perspiciatis unde omnis iste natus volup-tatem dolor emque laudantium...</p>
    <a class="btn btn-red about-btn" href="#">Read More</a>
  </div>

  <!-- services -->
  <div class="abs center eyebrow" style="top:1460px">Valmike</div>
  <h2 class="abs center heading" style="top:1484px">Our Services</h2>
  <article class="abs card" style="left:88px">
    <div class="card-img" role="img" aria-label="Business team in suits" style="background:linear-gradient(160deg,#8ea0ad,#3b4650)"></div>
    <div class="card-body"><h3 class="card-title">Executive<br>Protection</h3><p class="copy">Sed do eiusmod tempor aliqua. Ut enim ad minim veniam quis derit in voluptate velit</p></div>
  </article>
  <article class="abs card" style="left:435px">
    <div class="card-img" role="img" aria-label="Man in dark suit and sunglasses" style="background:linear-gradient(160deg,#6d5a44,#1e1f22)"></div>
    <div class="card-body"><h3 class="card-title">Covert<br>Protection</h3><p class="copy">Sed do eiusmod tempor aliqua. Ut enim ad minim veniam quis derit in voluptate velit</p></div>
  </article>
  <article class="abs card" style="left:782px">
    <div class="card-img" role="img" aria-label="City street with towers at night" style="background:linear-gradient(180deg,#2c4650,#18242a 60%,#6b4a30)"></div>
    <div class="card-body"><h3 class="card-title">Residential<br>Protection...</h3><p class="copy">Sed do eiusmod tempor aliqua. Ut enim ad minim veniam quis derit in voluptate velit</p></div>
  </article>

  <!-- iron finch -->
  <svg class="abs band" width="1200" height="640" viewBox="0 2100 1200 640" aria-hidden="true">
    <polygon points="0,2205 605,2112 1200,2197 1200,2668 0,2728" fill="#8e1316"/>
  </svg>
  <div class="abs band-art" role="img" aria-label="White line illustration of a suspension bridge" style="background:radial-gradient(ellipse at 70% 100%,rgba(255,255,255,.95) 0,rgba(255,255,255,.95) 32%,rgba(255,255,255,0) 33%)"></div>
  <div class="abs band-text">
    <div class="band-eyebrow">Iron Finch</div>
    <div class="band-title">Training and<br>Consulting</div>
    <p class="copy">Sed do eiusmod tempor incididunt ut labore et dolore magna aliqua. Ut enim ad minim veniam, quis derit in voluptate velit esse cillum dolore eu fugiat nullautur. Excepteur sint occaecat non proident, sunt in culpa qui officia...</p>
    <a class="btn band-btn" href="#">Read More</a>
  </div>

  <!-- testimonials -->
  <div class="abs center eyebrow" style="top:2760px">Testimonials</div>
  <h2 class="abs center heading" style="top:2786px">Customer Review</h2>
  <div class="abs avatar" role="img" aria-label="Portrait of the reviewer"></div>
  <div class="abs quote" aria-hidden="true">&#8220;</div>
  <div class="abs center reviewer">DANA WHITLOW</div>
  <div class="abs center role">MANAGER</div>
  <p class="abs review">Sed do eiusmod tempor incididunt ut labore et dolore magna aliqua. Ut enim ad minim veniam, quis derit in voluptate velit esse cillum dolore eu fugiat nullautur. Excepteur sint occaecat cupidatat</p>
  <div class="abs dots"><span></span><span class="on"></span><span></span></div>
  <div class="abs rule"></div>

  <!-- contact -->
  <div class="abs contact-photo" role="img" aria-label="Red suspension bridge tower against a pale sky and hills"></div>
  <div class="abs contact-head"><div class="eyebrow">Valmike</div><h2 class="heading">Contact Us</h2></div>
  <p class="abs contact-intro">To contact Valmike Group please email us or use the the contact form below.</p>
  <div class="abs field" style="left:575px;top:3415px;width:263px;height:37px">Name</div>
  <div class="abs field" style="left:847px;top:3415px;width:263px;height:37px">Email</div>
  <div class="abs field" style="left:575px;top:3458px;width:263px;height:37px">Phone</div>
  <div class="abs field" style="left:847px;top:3458px;width:263px;height:37px">Subject</div>
  <div class="abs field" style="left:575px;top:3502px;width:535px;height:133px">Message</div>
  <a class="abs btn btn-red submit" href="#">Submit Now</a>

  <!-- footer -->
  <svg class="abs footer" width="1200" height="491" viewBox="0 3800 1200 491" aria-hidden="true">
    <polygon points="0,3900 600,3808 1200,3900 1200,4291 0,4291" fill="#050505"/>
  </svg>
  <div class="abs brand footer-brand"><span class="brand-mark"></span>VALMIKE GROUP</div>
  <div class="abs socials"><span style="background:#3b5998"></span><span style="background:#1da1f2"></span><span style="background:#dd4b39"></span></div>
  <div class="abs col" style="left:433px"><div class="col-title">Quick Links</div>
    <ul><li>Home</li><li>About &nbsp;Us</li><li>Services</li><li>Iron Finch</li><li>Contact Us</li></ul></div>
  <div class="abs col" style="left:622px"><div class="col-title">Our Services</div>
    <ul><li>Terms and Condition</li><li>Privacy Policy</li><li>FAQ</li><li>Disclaimer</li><li>Customer Reviews</li></ul></div>
  <div class="abs col" style="left:855px"><div class="col-title">Contact Us</div>
    <div style="margin-top:22px">
      <div class="contact-item"><svg width="12" height="12" viewBox="0 0 12 12"><path d="M2 1l2 0 1 3-1.5 1a7 7 0 0 0 3.5 3.5L8 7l3 1v2c0 .6-.4 1-1 1A9 9 0 0 1 1 2c0-.6.4-1 1-1z" fill="#c41e24"/></svg><b>Phone</b><span>+01 555 014 2290</span></div>
      <div class="contact-item"><svg width="12" height="10" viewBox="0 0 12 10"><rect x="0" y="0" width="12" height="10" fill="#c41e24"/><polyline points="0,0 6,5 12,0" fill="none" stroke="#050505"/></svg><b>Email</b><span>hello@valmikegroup.test</span></div>
      <div class="contact-item"><svg width="10" height="13" viewBox="0 0 10 13"><path d="M5 0a5 5 0 0 1 5 5c0 3-5 8-5 8S0 8 0 5a5 5 0 0 1 5-5z" fill="#c41e24"/><circle cx="5" cy="5" r="1.8" fill="#050505"/></svg><b>Location</b><span>Some address line goes here<br>city name country</span></div>
    </div></div>
  <div class="abs footer-rule"></div>
  <div class="abs center copyright">© 2021 Copyright - Valmike Group All Rights Reserved</div>
  <svg class="abs to-top" width="46" height="46" viewBox="0 0 46 46" aria-hidden="true">
    <rect x="9" y="9" width="28" height="28" transform="rotate(45 23 23)" fill="#8e1316"/>
    <polyline points="17,26 23,20 29,26" fill="none" stroke="#fff" stroke-width="2"/>
  </svg>
</div>
</body>
</html>
```